Business Card Design for an Investment Company

We need a business card design for our private investment company, called Dunmore Equity. Dunmore Equity is an investments partnership that aims to acquire shares in listed companies with a view to influencing those companies through active dialogue in order to improve their value. We need designs that use the logo colors (blue, grey, white), we need both English and Arabic on the business cards (can be on one side or 2 sides). The final logo should communicate professionalism, conservatism (nothing too fancy or too cheesy), that we are smart, conservative and old school.

Target Market(s)

Investment companies

Industry/Entity Type

Investment

Contact Information for Business Card

Tariq Salmanuddin Farouqi
Senior Executive Officer

Harbor Court 07, Level 3, Office 214/12
QTFZ

+9714987650
tfarouqi@dunmore-equity.com
www.dunmore-equity.com

Requirements
Must have
• Logo to be placed on the left hand side of the business card
• for the Arabic, we only need to have the name and title so it can be accomodated on one side so we can have the other side with full color and logo. The arabic that needs to be used is the below:
• طارق سلمان الدين فاروقي
• المدير التنفيدي

```html
<!DOCTYPE html>
<html lang="en">
<head>
<meta charset="utf-8">
<title>Dunmore Equity – Business Card</title>
<link rel="stylesheet" href="https://fonts.googleapis.com/css2?family=Open+Sans:wght@400;600;700;800&family=Noto+Naskh+Arabic:wght@400;700&display=swap">
<style>
  :root {
    --stage: #e4e5e7;
    --card-dark: #58585a;
    --card-light: #ffffff;
    --brand-blue: #0a6aa1;
    --brand-grey: #58585a;
    --text-grey: #4a4a4c;
    --rule-white: #ffffff;
    --map-tone: #6a6a6c;
  }
  * { box-sizing: border-box; margin: 0; padding: 0; }
  html, body {
    width: 1200px; height: 900px; overflow: hidden;
    background: var(--stage);
    font-family: "Open Sans", Arial, sans-serif;
  }
  .stage {
    position: relative; width: 1200px; height: 900px;
    display: flex; flex-direction: column; align-items: center; justify-content: center; gap: 40px;
  }
  .card {
    position: relative; width: 660px; height: 377px; overflow: hidden;
    box-shadow: 0 6px 18px rgba(0,0,0,0.18);
  }

  /* Back side */
  .card--back { background: var(--card-dark); color: var(--rule-white); }
  .card__map {
    position: absolute; left: 70px; top: 40px; width: 520px; height: 250px;
    border-radius: 40px;
    background: radial-gradient(ellipse at center, var(--map-tone) 0%, rgba(106,106,108,0.4) 60%, rgba(88,88,90,0) 100%);
  }
  .wordmark {
    display: flex; align-items: center; gap: 12px;
    font-weight: 800; letter-spacing: -0.5px; white-space: nowrap;
  }
  .wordmark__square { width: 18px; height: 18px; flex: none; }
  .card--back .wordmark {
    position: absolute; left: 50%; top: 150px; transform: translateX(-50%);
    font-size: 44px; color: var(--rule-white);
  }
  .card--back .wordmark__square { background: var(--rule-white); }
  .rule { position: absolute; height: 2px; background: var(--rule-white); }
  .rule--right { left: 470px; right: 0; top: 222px; }
  .rule--left { left: 0; width: 210px; top: 300px; }
  .card__url {
    position: absolute; left: 226px; top: 288px;
    font-size: 15px; letter-spacing: 1px; color: var(--rule-white);
  }

  /* Front side */
  .card--front { background: var(--card-light); }
  .card--front .wordmark {
    position: absolute; left: 40px; top: 178px;
    font-size: 31px; color: var(--brand-blue);
  }
  .card--front .wordmark__square { background: var(--brand-grey); width: 14px; height: 14px; }
  .contact {
    position: absolute; left: 380px; top: 30px; color: var(--text-grey);
    font-size: 13.5px; line-height: 1.35;
  }
  .contact__name { font-size: 17px; font-weight: 700; color: var(--brand-blue); line-height: 1.2; }
  .contact__title { margin-bottom: 4px; }
  .contact__arabic {
    font-family: "Noto Naskh Arabic", "Open Sans", serif;
    direction: rtl; text-align: left; unicode-bidi: plaintext;
    line-height: 1.45; margin-bottom: 10px;
  }
  .contact__arabic-name { font-size: 15px; font-weight: 700; color: var(--brand-blue); }
  .contact__arabic-title { font-size: 13.5px; }
  .contact__address { margin-bottom: 2px; }
  .contact__list { list-style: none; }
  .contact__list li { display: flex; align-items: center; gap: 8px; }
  .contact__list svg { width: 13px; height: 13px; fill: var(--brand-blue); flex: none; }
  .bands { position: absolute; left: 0; top: 0; width: 660px; height: 377px; }
</style>
</head>
<body>
<main class="stage">

  <section class="card card--back" aria-label="Card back">
    <div class="card__map" role="img" aria-label="Faint dotted world map"></div>
    <div class="wordmark"><span class="wordmark__square"></span>Dunmore Equity</div>
    <span class="rule rule--right"></span>
    <span class="rule rule--left"></span>
    <p class="card__url">www.dunmore-equity.com</p>
  </section>

  <section class="card card--front" aria-label="Card front">
    <svg class="bands" viewBox="0 0 660 377" aria-hidden="true">
      <polygon points="470,296 660,240 660,258 488,308" fill="var(--brand-grey)"/>
      <polygon points="488,308 660,258 660,270 500,316" fill="var(--brand-blue)"/>
      <polygon points="200,377 212,322 440,322 470,348 660,292 660,377" fill="var(--brand-blue)"/>
    </svg>

    <div class="wordmark"><span class="wordmark__square"></span>Dunmore Equity</div>

    <div class="contact">
      <p class="contact__name">Tariq Salmanuddin Farouqi</p>
      <p class="contact__title">Senior Executive Officer</p>
      <div class="contact__arabic" lang="ar">
        <p class="contact__arabic-name">طارق سلمان الدين فاروقي</p>
        <p class="contact__arabic-title">المدير التنفيدي</p>
      </div>
      <p class="contact__address">Harbor Court 07, Level 3, Office 214/12<br>QTFZ</p>
      <ul class="contact__list">
        <li><svg viewBox="0 0 16 16"><path d="M3 1h3l1.5 4-2 1.2a9 9 0 0 0 4.3 4.3L11 8.5l4 1.5v3a2 2 0 0 1-2 2A12 12 0 0 1 1 3a2 2 0 0 1 2-2z"/></svg>+9714987650</li>
        <li><svg viewBox="0 0 16 16"><path d="M1 3h14v10H1zM2 4.2V5l6 4 6-4v-.8z"/></svg>tfarouqi@dunmore-equity.com</li>
        <li><svg viewBox="0 0 16 16"><path d="M8 1a7 7 0 1 0 0 14A7 7 0 0 0 8 1zm0 1.3c.9 1 1.5 2.3 1.7 3.7H6.3C6.5 4.6 7.1 3.3 8 2.3zM2.4 7.3h2.6a11 11 0 0 0 0 1.4H2.4a5.7 5.7 0 0 1 0-1.4zm3.9 0h3.4a9 9 0 0 1 0 1.4H6.3a9 9 0 0 1 0-1.4zm4.7 0h2.6a5.7 5.7 0 0 1 0 1.4H11a11 11 0 0 0 0-1.4zM6.3 10h3.4c-.2 1.4-.8 2.7-1.7 3.7-.9-1-1.5-2.3-1.7-3.7z"/></svg>www.dunmore-equity.com</li>
      </ul>
    </div>
  </section>

</main>
</body>
</html>
```